A new presentation to our clients

we are a Real Estate agency, our website is www.lirotama.com and it’s time to have a new, fashion and remarcable Business Card. we want to differentiate ourselves from other companies so we want a business card that differentiates us. we want the business card to impact our customers. in the competitive market that we have today, we have to be different and it is this difference that we seek

Target Market(s)

Real Estate Clients

Contact Information for Business Card

We search a totaly diferent card from the usual

Font styles to use
Sans Serif

Colors
e34197

Requirements
Must have
• Logo, adress, phone contact, e-mail, photo, and our website
Nice to have
• We would like to see a modern business card
Should not have
• Houses or building draws

```html
<!DOCTYPE html>
<html lang="en">
<head>
<meta charset="utf-8">
<title>Lirotama – Business Card</title>
<link rel="stylesheet" href="https://fonts.googleapis.com/css2?family=Poppins:wght@400;500&display=swap">
<style>
  :root {
    --brand-pink: #e60a96;
    --ink: #1c1c1c;
    --paper: #ffffff;
    --concrete-light: #e4e8e8;
    --concrete-mid: #c9cfcf;
    --concrete-floor: #dde1e1;
  }
  * { box-sizing: border-box; margin: 0; padding: 0; }
  html, body {
    width: 668px;
    height: 1200px;
    overflow: hidden;
    background: var(--paper);
  }
  .card {
    position: relative;
    width: 668px;
    height: 1200px;
    background: var(--paper);
    font-family: "Poppins", sans-serif;
  }
  .card__photo {
    position: absolute;
    left: 0;
    top: 0;
    width: 668px;
    height: 750px;
    background:
      linear-gradient(180deg,
        var(--concrete-light) 0%,
        var(--concrete-mid) 45%,
        var(--concrete-mid) 84%,
        var(--concrete-floor) 85%,
        #eceeee 100%);
  }
  .card__frame {
    position: absolute;
    left: 29px;
    top: 27px;
    width: 612px;
    height: 1142px;
    border: 3px solid var(--brand-pink);
  }
  .card__brand {
    position: absolute;
    left: 0;
    right: 0;
    top: 160px;
    text-align: center;
    font-size: 82px;
    font-weight: 500;
    letter-spacing: 1px;
    color: var(--brand-pink);
    line-height: 1;
  }
  .contact {
    position: absolute;
    left: 87px;
    top: 780px;
    width: 502px;
    list-style: none;
  }
  .contact__row {
    display: flex;
    align-items: flex-start;
    border-bottom: 2px solid var(--brand-pink);
  }
  .contact__row:last-child { border-bottom: none; }
  .contact__row--address { height: 101px; padding-top: 22px; }
  .contact__row--email   { height: 86px;  padding-top: 30px; }
  .contact__row--web     { height: 89px;  padding-top: 32px; }
  .contact__row--phone   { height: 89px;  padding-top: 33px; }
  .contact__label {
    width: 193px;
    padding-left: 27px;
    padding-top: 3px;
    font-size: 17px;
    font-weight: 400;
    color: var(--brand-pink);
  }
  .contact__value {
    font-size: 20px;
    font-weight: 400;
    color: var(--ink);
    line-height: 1.3;
  }
</style>
</head>
<body>
  <div class="card">
    <div class="card__photo" role="img" aria-label="Photograph of a bare grey concrete wall with rows of tie holes above a pale concrete floor"></div>
    <div class="card__brand">Lirotama</div>
    <ul class="contact">
      <li class="contact__row contact__row--address">
        <span class="contact__label">Adress</span>
        <span class="contact__value">Rua das Acácias, 148<br>4410-052, Vila Nova de Gaia</span>
      </li>
      <li class="contact__row contact__row--email">
        <span class="contact__label">E-mail</span>
        <span class="contact__value">geral@lirotama.com</span>
      </li>
      <li class="contact__row contact__row--web">
        <span class="contact__label">Web-site</span>
        <span class="contact__value">www.lirotama.com</span>
      </li>
      <li class="contact__row contact__row--phone">
        <span class="contact__label">Phone</span>
        <span class="contact__value">(+351) 220 418 536</span>
      </li>
    </ul>
    <div class="card__frame"></div>
  </div>
</body>
</html>
```